Financial Services Business Card Design

We are a financial services company Based in London, offering Short term Funding Solutions for companies, raising anywhere between £20,000 and £25million pounds.

The Card must have a professional look as it is going to be handed out to professionals I.E Solicitors, Accountants, Company directors and Business owners.

See Attached our company Logo

Industry/Entity Type

Business

Contact Information for Business Card

Lewis Thorncroft
Suite 41
R K House
Bramblecote Lane
Ashcombe
HP19 4QX

```html
<!DOCTYPE html>
<html lang="en">
<head>
<meta charset="utf-8">
<title>Harrowgate Bridge Finance – Business Card</title>
<link rel="stylesheet" href="https://fonts.googleapis.com/css2?family=Arimo:wght@400;700&display=swap">
<style>
  :root {
    --stage: #e9e7e3;
    --card-white: #ffffff;
    --brand-blue: #1f6db5;
    --brand-green: #3aa83a;
    --card-black: #0b0c0e;
    --ink-white: #ffffff;
  }
  * { box-sizing: border-box; margin: 0; padding: 0; }
  html, body {
    width: 1200px; height: 892px; overflow: hidden;
    background: var(--stage);
    font-family: "Arimo", Arial, sans-serif;
  }
  .stage {
    position: relative; width: 1200px; height: 892px;
    display: flex; justify-content: center; align-items: center; gap: 80px;
  }
  .card {
    width: 340px; height: 540px;
    box-shadow: 0 10px 30px rgba(0,0,0,.18);
    position: relative; overflow: hidden;
  }
  /* Front */
  .card-front { background: var(--card-white); display: flex; flex-direction: column; }
  .brand-area {
    height: 190px; display: flex; align-items: center; justify-content: center; gap: 10px;
    padding: 0 20px;
  }
  .brand-mark { width: 16px; height: 16px; border-radius: 50%; background: var(--brand-green); flex: none; }
  .brand-name {
    color: var(--brand-blue); font-weight: 700; font-size: 24px; line-height: 1.15;
    text-align: center; letter-spacing: .5px;
  }
  .name-band {
    background: var(--brand-green); color: var(--ink-white);
    height: 62px; display: flex; align-items: center; padding-left: 34px;
    font-size: 28px; font-weight: 400; letter-spacing: .3px; white-space: nowrap;
  }
  .contact-list { list-style: none; margin-top: 14px; }
  .contact-row {
    background: var(--brand-blue); color: var(--ink-white);
    display: flex; align-items: center; gap: 14px;
    padding: 0 18px 0 26px; height: 44px; margin-bottom: 14px;
    font-size: 15px; letter-spacing: .2px; white-space: nowrap;
  }
  .contact-row.address { height: 62px; line-height: 1.35; }
  .icon {
    width: 18px; height: 18px; background: var(--ink-white); border-radius: 3px; flex: none;
    display: flex; align-items: center; justify-content: center;
  }
  .icon svg { width: 12px; height: 12px; }
  .foot-strip { position: absolute; left: 0; right: 0; bottom: 0; height: 22px; background: var(--card-black); }
  /* Back */
  .card-back {
    background: var(--card-black);
    display: flex; align-items: center; justify-content: center; gap: 10px;
  }
  .card-back .brand-name { font-size: 26px; }
</style>
</head>
<body>
<main class="stage">
  <section class="card card-front" aria-label="Business card front">
    <div class="brand-area">
      <span class="brand-mark" aria-hidden="true"></span>
      <span class="brand-name">Harrowgate Bridge<br>Finance</span>
    </div>
    <div class="name-band">Lewis Thorncroft</div>
    <ul class="contact-list">
      <li class="contact-row">
        <span class="icon"><svg viewBox="0 0 12 12"><path d="M3 1l2 2-1 1.5c.6 1.3 1.4 2.1 2.6 2.6L8 6l2 2-1.4 1.6C5.5 9.6 2.4 6.5 2 3.4z" fill="#1f6db5"/></svg></span>
        07700 900418
      </li>
      <li class="contact-row">
        <span class="icon"><svg viewBox="0 0 12 12"><rect x="1" y="2.5" width="10" height="7" fill="none" stroke="#1f6db5" stroke-width="1.2"/><path d="M1 2.5l5 4 5-4" fill="none" stroke="#1f6db5" stroke-width="1.2"/></svg></span>
        hello@harrowgate.co.uk
      </li>
      <li class="contact-row">
        <span class="icon"><svg viewBox="0 0 12 12"><circle cx="6" cy="6" r="4.6" fill="none" stroke="#1f6db5" stroke-width="1.1"/><ellipse cx="6" cy="6" rx="2" ry="4.6" fill="none" stroke="#1f6db5" stroke-width="1"/><path d="M1.4 6h9.2" stroke="#1f6db5" stroke-width="1"/></svg></span>
        www.harrowgatefinance.co.uk
      </li>
      <li class="contact-row address">
        <span class="icon"><svg viewBox="0 0 12 12"><path d="M6 11S2.3 6.8 2.3 4.6a3.7 3.7 0 017.4 0C9.7 6.8 6 11 6 11z" fill="#1f6db5"/><circle cx="6" cy="4.6" r="1.3" fill="#fff"/></svg></span>
        <span>Suite 41 R K House Bramblecote<br>Lane Ashcombe HP19 4QX</span>
      </li>
    </ul>
    <div class="foot-strip"></div>
  </section>

  <section class="card card-back" aria-label="Business card back">
    <span class="brand-mark" aria-hidden="true"></span>
    <span class="brand-name">Harrowgate Bridge<br>Finance</span>
  </section>
</main>
</body>
</html>
```